Graphic Design - Paperback Book Cover

The graphic design project is to create a book cover and potentially an accompanying logo for a book called The Boundless Compass: A Field Guide for Steering Through a Season of Shifting Tides. The title is a working title and may change slightly. The book presents 10 capabilities that organizational leaders should have to be able to lead in a world filled with uncertainties. The main themes are the following:• Leaders need to be clear and focused about the overall mission, but also need to make strategic decisions with a diversity of opinions and options.• Leaders must anticipate where they will need to adapt in implementing strategy.• Leaders need to create a culture that promotes trust and agility.• Leaders need to be vigilant and look for early indicators of change. Show intellectual curiosity.• Leaders should be willing to experiment and learn from the experiments.The book is designed as a handbook. This will be a self published business book.The below graphic provides what are the key concepts representing each letter of “BOUNDLESS”. The right-hand column provides key words / phrases associated with the concepts.
Updates

Need extra days to review

Need extra days to review

Target Market(s)

Mid to Senior level executives at global companies across industries.

Colors

Designer to choose colors to be used in the design.

Requirements
Must have
• No must haves.
Nice to have
• Wide open on the design.

```html
<!DOCTYPE html>
<html lang="en">
<head>
<meta charset="utf-8">
<title>The Boundless Compass — Paperback Cover</title>
<link rel="stylesheet" href="https://fonts.googleapis.com/css2?family=Barlow+Condensed:wght@300;400;500&display=swap">
<style>
  :root {
    --backdrop: #e6e6e7;
    --rose-light: #e9dfe0;
    --rose-mid: #c7adb0;
    --maze-top: #c9787f;
    --maze-glow: #e6c7ca;
    --maze-deep: #7e4a50;
    --ink: #222222;
    --paper: #ffffff;
  }
  * { margin: 0; padding: 0; box-sizing: border-box; }
  html, body {
    width: 1200px; height: 1200px; overflow: hidden;
    background: var(--backdrop);
  }
  .cover {
    position: absolute; left: 154px; top: 50px;
    width: 892px; height: 1100px; overflow: hidden;
    background: linear-gradient(155deg, var(--rose-mid) 30%, var(--rose-light) 75%);
    font-family: "Barlow Condensed", sans-serif;
    text-align: center;
  }
  .cover-art { position: absolute; inset: 0; width: 100%; height: 100%; }
  .authors, .title-line, .subtitle {
    position: absolute; left: 0; width: 100%; line-height: 1;
  }
  .authors {
    top: 60px; font-size: 45px; font-weight: 400; color: var(--ink);
    line-height: 52px; letter-spacing: 0.5px;
  }
  .title-line { font-weight: 500; letter-spacing: -1px; }
  .title-the { top: 298px; font-size: 120px; color: var(--paper); }
  .title-key { top: 377px; font-size: 214px; color: var(--ink); }
  .title-end { top: 541px; font-size: 214px; color: var(--paper); }
  .subtitle {
    top: 865px; left: 250px; width: 392px;
    font-size: 37px; font-weight: 300; line-height: 50px; color: var(--ink);
  }
</style>
</head>
<body>
  <main class="cover">
    <svg class="cover-art" viewBox="0 0 892 1100" role="img" aria-label="Isometric maze of rose-coloured walls rising from the upper left">
      <defs>
        <linearGradient id="mazeTone" x1="0" y1="0" x2="1" y2="1">
          <stop offset="0" stop-color="var(--maze-top)"/>
          <stop offset="0.35" stop-color="var(--maze-glow)"/>
          <stop offset="0.75" stop-color="var(--maze-deep)"/>
        </linearGradient>
      </defs>
      <polygon points="0,0 892,0 892,323 0,913" fill="url(#mazeTone)"/>
    </svg>

    <p class="authors">AUTOR NAME &amp;<br>OTHER AUTOR NAME</p>

    <h1>
      <span class="title-line title-the">THE</span>
      <span class="title-line title-key">BOUNDLESS</span>
      <span class="title-line title-end">COMPASS</span>
    </h1>

    <p class="subtitle">A Field Guide for Steering Through a Season of Shifting Tides</p>
  </main>
</body>
</html>
```